I need a new business card design for my pharmacy.

I need a business card design. I will include my logo.
The card needs to be readable. I prefer to have my logo on one side along with my website, the other side includes the other information. Please use combination of black, neon green, white, and silver. This needs to catch the eye but yet be clearly visible and legible. Thanks

Industry/Entity Type

Pharmacy

Contact Information for Business Card

It needs to have the following information listed:
Mel's Apothecary Owner/Pharm D.
7134 North Brook Lane
Sioux Falls, SD 57231
Phone 605-318-6207
Fax 605-318-6209
email: mel@melsapothecary-example.com
www.melsapothecary-example.com
Store hours Monday-Friday 8 am- 7 pm
Saturday 8 am- 12 pm
Sunday Closed
Please utilize the colors black, white, and neon green, maybe silver.

Requirements
Must have
• It needs to be easily readable!
Nice to have
• It should catch the eye.
Should not have
• Do not use any other colors except listed: black, neon green, white, & silver.

```html
<!DOCTYPE html>
<html lang="en">
<head>
<meta charset="utf-8">
<title>Mel's Apothecary – Business Card Front</title>
<link href="https://fonts.googleapis.com/css2?family=Encode+Sans+Semi+Condensed:wght@600&family=Source+Serif+4:ital,wght@1,300&display=swap" rel="stylesheet">
<style>
  :root {
    --paper: #ffffff;
    --card: #000000;
    --neon-green: #a6ce39;
    --silver: #c9c9c9;
  }
  * { margin: 0; padding: 0; box-sizing: border-box; }
  html, body {
    width: 1200px;
    height: 1000px;
    overflow: hidden;
    background: var(--paper);
  }
  .card {
    position: absolute;
    left: 46px;
    top: 65px;
    width: 1107px;
    height: 867px;
    background: var(--card);
    overflow: hidden;
  }
  .brand-mark {
    position: absolute;
    left: 110px;
    top: 310px;
  }
  .brand-divider {
    position: absolute;
    left: 355px;
    top: 275px;
    width: 3px;
    height: 243px;
    background: var(--neon-green);
  }
  .brand-name {
    position: absolute;
    left: 405px;
    top: 330px;
    width: 640px;
    font-family: "Encode Sans Semi Condensed", sans-serif;
    font-weight: 600;
    font-size: 84px;
    line-height: 1;
    letter-spacing: -2px;
    color: var(--neon-green);
    white-space: nowrap;
  }
  .contact-line {
    position: absolute;
    left: 99px;
    right: 70px;
    top: 740px;
    display: flex;
    justify-content: space-between;
    gap: 40px;
    font-family: "Source Serif 4", serif;
    font-style: italic;
    font-weight: 300;
    font-size: 28px;
    color: var(--silver);
    white-space: nowrap;
  }
</style>
</head>
<body>
  <main class="card">
    <svg class="brand-mark" width="190" height="190" viewBox="0 0 190 190" aria-hidden="true">
      <circle cx="95" cy="95" r="80" fill="none" stroke="var(--neon-green)" stroke-width="12"/>
    </svg>
    <div class="brand-divider"></div>
    <h1 class="brand-name">Mel's Apothecary</h1>
    <p class="contact-line">
      <span class="website">www.melsapothecary-example.com</span>
      <span class="email">mel@melsapothecary-example.com</span>
    </p>
  </main>
</body>
</html>
```